Business Cards

I'm an contractor and consultant in IT Project management. I'd like a design for business cards.
In my work I mostly meet clients, peer project managers and technical staff. I usually exchange business cards at technical conventions or when networking.
I provide services that are:
- Updated, always with a fresh look on technology
- Solid and reliable
- Flexible schedule and always available
The current business card has been attached to provide information.
Target Market(s)
IT managers, IT project managers, consultants, recruitment staff. Age 30-45 years. College/University degree.
Industry/Entity Type
Contractor
Colors
Designer to choose colors to be used in the design.
Requirements
Must have
- Two sides, one side with personal information and the other side with company name.
Text in Norwegian, including Norwegian characters
Nice to have
- It should be possible for non-Norwegian speakers to read the contact details.

```html
<!DOCTYPE html>
<html lang="no">
<head>
<meta charset="utf-8">
<title>Lindvik Consulting AS – Visittkort</title>
<link rel="stylesheet" href="https://fonts.googleapis.com/css2?family=EB+Garamond:wght@400;600&display=swap">
<style>
  :root {
    --bg: #d9d6cf;
    --card: #2a2a2a;
    --card-shade: #323232;
    --accent: #e5c31e;
    --text-light: #f2f2f2;
    --text-dark: #222222;
  }
  * { margin: 0; padding: 0; box-sizing: border-box; }
  html, body { width: 1200px; height: 1000px; overflow: hidden; }
  body {
    background: var(--bg);
    font-family: "EB Garamond", Georgia, serif;
    display: flex;
    align-items: center;
    justify-content: center;
    gap: 50px;
  }
  .card {
    position: relative;
    width: 540px;
    height: 310px;
    border-radius: 26px;
    background: radial-gradient(circle at 40% 35%, var(--card-shade), var(--card) 70%);
    overflow: hidden;
    box-shadow: 0 10px 24px rgba(0,0,0,0.25);
  }
  .brand { color: var(--accent); font-weight: 600; line-height: 1; white-space: nowrap; }
  .brand-name { font-size: 34px; letter-spacing: 0.5px; }
  .brand-tag { font-size: 17px; font-weight: 400; margin-top: 4px; text-align: center; }

  /* Front side */
  .front .brand {
    position: absolute; left: 0; right: 0; top: 110px;
    text-align: center;
  }
  .front .web {
    position: absolute; left: 0; right: 0; bottom: 46px;
    text-align: center; color: var(--text-light); font-size: 17px;
  }
  .front .band {
    position: absolute; left: 0; right: 0; bottom: 0; height: 30px;
    background: var(--accent);
    border-radius: 0 60px 0 0 / 0 20px 0 0;
  }

  /* Back side */
  .back .person {
    position: absolute; left: 36px; top: 34px;
    color: var(--text-light); font-size: 16px; line-height: 1.5;
    white-space: nowrap;
  }
  .back .person .role { color: var(--accent); }
  .back .brand { position: absolute; right: 36px; top: 140px; text-align: right; }
  .back .contact-band {
    position: absolute; left: 0; right: 0; bottom: 40px; height: 42px;
    background: var(--accent);
    display: flex; align-items: center; justify-content: space-between;
    padding: 0 18px;
  }
  .contact-item {
    display: flex; align-items: center; gap: 7px;
    color: var(--text-dark); font-size: 13px; font-weight: 600;
    white-space: nowrap; flex: none;
  }
  .contact-icon { width: 20px; height: 20px; flex: none; }
</style>
</head>
<body>

  <section class="card front" aria-label="Forside">
    <div class="brand">
      <div class="brand-name">Lindvik Consulting AS</div>
      <div class="brand-tag">IT Implementering</div>
    </div>
    <div class="web">www.lindvikconsulting.no</div>
    <div class="band"></div>
  </section>

  <section class="card back" aria-label="Bakside">
    <div class="person">
      <div>Eirik Holmen <span class="role">| IT Rådgiver</span></div>
      <div>Brattbergveien 14 0471 Oslo</div>
    </div>
    <div class="brand">
      <div class="brand-name">Lindvik Consulting AS</div>
      <div class="brand-tag">IT Implementering</div>
    </div>
    <div class="contact-band">
      <div class="contact-item">
        <svg class="contact-icon" viewBox="0 0 22 22" aria-hidden="true">
          <circle cx="11" cy="11" r="11" fill="#2a2a2a"/>
          <rect x="8" y="5" width="6" height="12" rx="1" fill="none" stroke="#e5c31e" stroke-width="1.4"/>
          <line x1="10" y1="15" x2="12" y2="15" stroke="#e5c31e" stroke-width="1.2"/>
        </svg>
        912-45-678
      </div>
      <div class="contact-item">
        <svg class="contact-icon" viewBox="0 0 22 22" aria-hidden="true">
          <circle cx="11" cy="11" r="11" fill="#2a2a2a"/>
          <rect x="5.5" y="7.5" width="11" height="7.5" fill="none" stroke="#e5c31e" stroke-width="1.3"/>
          <polyline points="5.5,7.5 11,12 16.5,7.5" fill="none" stroke="#e5c31e" stroke-width="1.3"/>
        </svg>
        eirik@lindvikconsulting.no
      </div>
      <div class="contact-item">
        <svg class="contact-icon" viewBox="0 0 22 22" aria-hidden="true">
          <circle cx="11" cy="11" r="11" fill="#2a2a2a"/>
          <circle cx="11" cy="11" r="6" fill="none" stroke="#e5c31e" stroke-width="1.2"/>
          <ellipse cx="11" cy="11" rx="2.6" ry="6" fill="none" stroke="#e5c31e" stroke-width="1"/>
          <line x1="5" y1="11" x2="17" y2="11" stroke="#e5c31e" stroke-width="1"/>
        </svg>
        www.lindvikconsulting.no
      </div>
    </div>
  </section>

</body>
</html>
```